Business card design for a content marketing agency

Need a business card design suitable for a digital marketing agency. Needs to be a bold and creative, high quality design that exudes expertise and professionalism, and instills in prospective new customers a sense of confidence that we are the right company to do business with. Specifications must meet PrintNorvo requirement for extra thick matte stock. Needs to incorporate logo, tagline, name, title, website url, address, city, state, zip code, and mobile number.. I spec'd s single side design but I'm to a double sided design if it's strong and compelling. I like the use of icons associated with contact info, but it's not a requirement. Mostly, the design needs to command attention because it's so good or unusual. I have all kinds of files in large thru small sizes in jpg andpgn. pick from what you need, and let me know if you have questions.

Target Market(s)

CEO, Mktg VP's and small to medium size tech and prof'l service businesses

Industry/Entity Type

Marketing

Contact Information for Business Card

Perry Lindqvist
Chief Executive Officer
418 Wexcombe Lane
Brenwick, MA 01794
perry@quelmarketing.example
www.quelmarketing.example
978-555-2716

Font styles to use
Sans Serif

Colors
0692cd
9bcb3c

Requirements
Must have
• Tagline is "Outreach That Clients Believe".
• Needs to be a bold and creative, high quality design that exudes expertise and professionalism, and instills in prospective new customers a sense of confidence that we are the right company to do business with. Specifications must meet PrintNorvo requirement for extra thick matte stock. Needs to incorporate logo, tagline, name, title, website url, address, city, state, zip code, and mobile number..
Nice to have
• I spec'd s single side design but I'm open to a double sided design if it's strong and compelling. I like the use of icons associated with contact info, but it's not a requirement.
Should not have
• Chose colors that are the same and/or compatible with colors in the logo

```html
<!DOCTYPE html>
<html lang="en">
<head>
<meta charset="utf-8">
<title>Quel Marketing – Business Card</title>
<link rel="stylesheet" href="https://fonts.googleapis.com/css2?family=Open+Sans:wght@400;600&display=swap">
<style>
  :root {
    --stage: #e9e9eb;
    --card: #111213;
    --card-edge: #1c1d1f;
    --blue: #1f8fd6;
    --white: #f4f5f6;
    --muted: #c9ccd0;
    --divider: #5a5d62;
  }
  * { margin: 0; padding: 0; box-sizing: border-box; }
  html, body { width: 1200px; height: 814px; overflow: hidden; }
  body {
    background: var(--stage);
    font-family: "Open Sans", Arial, sans-serif;
    display: flex;
    align-items: center;
    justify-content: center;
    gap: 40px;
  }
  .card {
    width: 525px;
    height: 300px;
    background: var(--card);
    border: 1px solid var(--card-edge);
    border-radius: 3px;
    box-shadow: 0 10px 28px rgba(0,0,0,.25);
    position: relative;
  }
  .card--contact { display: flex; align-items: center; }
  .brand {
    width: 232px;
    display: flex;
    align-items: center;
    justify-content: center;
    gap: 10px;
  }
  .brand__dot {
    width: 14px; height: 14px;
    border-radius: 50%;
    background: var(--blue);
    flex: none;
  }
  .brand__name {
    color: var(--white);
    font-size: 22px;
    font-weight: 400;
    letter-spacing: .2px;
    white-space: nowrap;
  }
  .divider {
    width: 1px;
    height: 150px;
    background: linear-gradient(to bottom, transparent, var(--divider) 15%, var(--divider) 85%, transparent);
  }
  .contact { padding-left: 20px; color: var(--muted); font-size: 13px; line-height: 1.55; }
  .contact__name { color: var(--blue); font-size: 18px; font-weight: 600; line-height: 1.3; }
  .contact__title { color: var(--white); margin-bottom: 2px; }
  .contact__list { list-style: none; margin-top: 4px; }
  .contact__item { display: flex; align-items: center; gap: 8px; white-space: nowrap; }
  .contact__icon { width: 12px; height: 12px; fill: var(--blue); flex: none; }
  .card--brand {
    display: flex;
    flex-direction: column;
    align-items: center;
    justify-content: center;
    gap: 40px;
  }
  .brand--large { width: auto; gap: 14px; }
  .brand--large .brand__name { font-size: 34px; }
  .brand--large .brand__dot { width: 20px; height: 20px; }
  .tagline { color: var(--blue); font-size: 15px; font-weight: 400; }
</style>
</head>
<body>
  <section class="card card--contact" aria-label="Card front">
    <div class="brand">
      <span class="brand__dot"></span>
      <span class="brand__name">Quel Marketing</span>
    </div>
    <div class="divider"></div>
    <div class="contact">
      <p class="contact__name">Perry Lindqvist</p>
      <p class="contact__title">Chief Executive Officer</p>
      <p>418 Wexcombe Lane</p>
      <p>Brenwick, MA 01794</p>
      <ul class="contact__list">
        <li class="contact__item">
          <svg class="contact__icon" viewBox="0 0 24 24" aria-hidden="true"><path d="M6.6 10.8a15.1 15.1 0 0 0 6.6 6.6l2.2-2.2a1 1 0 0 1 1-.25 11.4 11.4 0 0 0 3.6.57 1 1 0 0 1 1 1V20a1 1 0 0 1-1 1A17 17 0 0 1 3 4a1 1 0 0 1 1-1h3.5a1 1 0 0 1 1 1c0 1.25.2 2.45.57 3.57a1 1 0 0 1-.25 1z"/></svg>
          <span>978-555-2716</span>
        </li>
        <li class="contact__item">
          <svg class="contact__icon" viewBox="0 0 24 24" aria-hidden="true"><path d="M2 5h20v14H2z M3.5 6.5 12 13l8.5-6.5" stroke="#111213" stroke-width="1.6"/></svg>
          <span>perry@quelmarketing.example</span>
        </li>
        <li class="contact__item">
          <svg class="contact__icon" viewBox="0 0 24 24" aria-hidden="true"><circle cx="12" cy="12" r="10"/><path d="M2 12h20M12 2c3 3 3 17 0 20M12 2c-3 3-3 17 0 20" stroke="#111213" stroke-width="1.4" fill="none"/></svg>
          <span>www.quelmarketing.example</span>
        </li>
      </ul>
    </div>
  </section>

  <section class="card card--brand" aria-label="Card back">
    <div class="brand brand--large">
      <span class="brand__dot"></span>
      <span class="brand__name">Quel Marketing</span>
    </div>
    <p class="tagline">Outreach That Clients Believe</p>
  </section>
</body>
</html>
```